Financial & Tax Strategies

need to get a word press site with existing domains and condense existing content on existing site, make new site dynamic, need mobile too......need to take info from my brimlo website and get modern, relevant site, less verbose on first page, way more things to click and engage people. Would like it to look like this , but with my color scheme and not quite as busy looking. I like much of the content on my tabs. Want maximize by seo capabilities on their as well. The number one thing I can say is to go to my existing website and get content, logo, etc there … www.pineridgealdergroup.com .

Target Market(s)

Those 40 -65, business owners for at least 5 years. Higher net worth.

Number of Pages Required

5+ page

Font styles to use
Sans Serif

Colors
f04a50
e4daeb
ffffff

Requirements
Must have
• seo maximized, lots of places to click on to contact us, calls to action, relevant, conservative, want it to look like this and have the function as well.....slight variation on messaging, but like the simplicity on first view. https://www.dorvettalbrook.com/
Nice to have
• Some area along right side where videos we do will be.
Should not have
• feel too busy, but still have lots of opportunities to engage.

```html
<!DOCTYPE html>
<html lang="en">
<head>
<meta charset="utf-8">
<title>Pine Ridge Alder Group – Financial &amp; Tax Strategies</title>
<link href="https://fonts.googleapis.com/css2?family=Roboto:wght@300;400;500;700&family=Arimo:wght@400;700&display=swap" rel="stylesheet">
<style>
:root{
  --red:#e8282e;
  --red-soft:#f04a50;
  --ink:#333333;
  --muted:#666666;
  --band:#3b3b3b;
  --footer:#3a3a3a;
  --light:#f4f4f4;
  --line:#d8d8d8;
  --white:#ffffff;
  --hero-a:#0d2238;
  --hero-b:#1d4a78;
}
*{box-sizing:border-box;margin:0;padding:0}
html,body{width:1200px;height:3965px;overflow:hidden}
body{font-family:"Roboto",Arial,sans-serif;color:var(--ink);background:var(--white);position:relative}

/* header */
.site-header{position:absolute;top:0;left:0;width:1200px;height:100px;background:var(--white)}
.menu-toggle{position:absolute;left:80px;top:36px;width:26px}
.menu-toggle span{display:block;height:3px;background:#555;margin-bottom:6px}
.brand{position:absolute;left:496px;top:24px;display:flex;align-items:center;gap:12px}
.brand-dot{width:48px;height:48px;border-radius:50%;background:#8a8a8a}
.brand-name{font-weight:700;font-size:22px;line-height:24px;color:#444}
.header-call{position:absolute;left:952px;top:28px;display:flex;gap:10px;align-items:center}
.header-call .ic{width:28px;height:28px;border-radius:50%;background:var(--red);display:flex;align-items:center;justify-content:center}
.header-call p{font-size:13px;line-height:15px;color:var(--red)}
.header-call p b{color:#222;font-weight:400}

/* hero */
.hero{position:absolute;top:100px;left:0;width:1200px;height:534px;background:radial-gradient(ellipse at 65% 55%,#2c6aa6 0%,var(--hero-b) 35%,var(--hero-a) 80%)}
.hero-caption{position:absolute;left:362px;top:209px;width:476px;height:116px;background:rgba(20,30,45,.7);color:var(--white);font-size:29px;line-height:36px;text-align:center;display:flex;align-items:center;justify-content:center}
.hero-arrow{position:absolute;top:242px}
.hero-dots{position:absolute;left:582px;top:502px;display:flex;gap:8px}
.hero-dots i{width:8px;height:8px;border-radius:50%;background:rgba(255,255,255,.5)}
.hero-dots i:first-child{background:var(--white)}

/* services */
.services-title{position:absolute;top:688px;width:1200px;text-align:center;font-size:31px;font-weight:400}
.service{position:absolute;display:flex;align-items:center;gap:14px;font-size:29px;font-weight:300;color:#333}

/* contact band */
.contact-band{position:absolute;top:1110px;left:0;width:1200px;height:190px;background:linear-gradient(90deg,#3a3634,#5a5450 50%,#3a3634);color:var(--white);text-align:center}
.contact-band h2{font-size:31px;font-weight:700;margin-top:36px}
.contact-row{display:flex;justify-content:center;gap:40px;margin-top:16px;font-size:33px;font-weight:700}
.contact-row span{display:flex;align-items:center;gap:14px}
.round-ic{width:56px;height:56px;border-radius:50%;background:var(--red);display:inline-flex;align-items:center;justify-content:center}
.contact-band .tag{font-size:19px;font-weight:700;margin-top:12px}

/* features */
.features{position:absolute;top:1300px;left:0;width:1200px;height:333px;background:var(--light)}
.feature{position:absolute;top:48px;width:238px;height:218px;background:var(--white);border-radius:16px;box-shadow:0 2px 10px rgba(0,0,0,.06);text-align:center;padding-top:58px}
.feature p{font-size:15px;line-height:19px;color:#555;padding:0 18px;margin-top:14px}

/* section bands */
.section-band{position:absolute;left:0;width:1200px;background:var(--band);color:var(--white);text-align:center;font-size:33px;font-weight:400;display:flex;align-items:center;justify-content:center}

/* blog cards */
.blog-card{position:absolute;top:1736px;width:333px;height:479px;background:var(--white);box-shadow:0 2px 12px rgba(0,0,0,.1);padding:12px}
.blog-media{width:309px;height:206px}
.blog-card h3{font-size:16px;font-weight:700;margin-top:18px;color:#222}
.blog-card p{font-size:13px;line-height:17px;color:#444;margin-top:10px}
.pill{position:absolute;background:var(--red);color:var(--white);border-radius:20px;font-size:14px;font-weight:500;display:flex;align-items:center;justify-content:center}

/* calculator */
.calc{position:absolute;top:2492px;left:82px;width:1039px;height:309px;border:1px solid var(--line);font-family:"Arimo",Arial,sans-serif;background:var(--white)}
.calc-row{border-bottom:1px solid var(--line);padding:6px 10px;position:relative}
.calc-row:last-child{border-bottom:none}
.calc-row h4{font-size:27px;font-weight:700;color:#111;line-height:32px}
.calc-row p{font-size:24px;line-height:28px;color:#111}
.calc-row .ctl{position:absolute;right:8px;top:10px;font-size:18px;color:#336}

/* testimonials */
.testimonial{position:absolute;top:2965px;width:301px;height:339px;background:var(--white);border-radius:12px;box-shadow:0 2px 12px rgba(0,0,0,.1);text-align:center;padding-top:32px}
.avatar{width:100px;height:100px;border-radius:50%;margin:0 auto;background:linear-gradient(160deg,#c9ccd1,#7a808a)}
.testimonial h5{font-size:15px;font-weight:400;margin-top:16px;color:#222}
.testimonial p{font-size:13px;line-height:16px;color:#444;padding:0 22px;margin-top:22px}
.t-dots{position:absolute;top:3326px;left:581px;display:flex;gap:8px}
.t-dots i{width:8px;height:8px;border-radius:50%;background:#e99}
.t-dots i:first-child{background:var(--red)}

/* quick email */
.quick-email{position:absolute;top:3410px;left:299px;width:428px;height:37px;border:1px solid #eee;border-radius:20px;font-size:13px;color:#666;padding:10px 16px;background:var(--white)}
.call-us{position:absolute;top:3480px;width:1200px;display:flex;justify-content:center;align-items:center;gap:16px;font-size:31px;font-weight:700;color:#333}

/* footer */
.site-footer{position:absolute;top:3581px;left:0;width:1200px;height:317px;background:var(--footer);color:var(--white)}
.foot-brand{position:absolute;left:74px;top:64px;display:flex;align-items:center;gap:10px;font-size:24px;font-weight:700;line-height:25px}
.foot-brand .dot{width:44px;height:44px;border-radius:50%;background:#bbb}
.foot-about{position:absolute;left:74px;top:134px;width:230px;font-size:13px;line-height:16px;color:#ddd}
.foot-col{position:absolute;top:66px}
.foot-col h6{font-size:16px;font-weight:500;margin-bottom:12px}
.foot-col ul{list-style:disc;padding-left:18px;font-size:13px;line-height:16px}
.foot-col .addr{font-size:13px;line-height:22px}
.field{background:var(--white);color:#555;font-size:12px;padding:6px 8px;height:30px}
.bottom-bar{position:absolute;top:3898px;left:0;width:1200px;height:67px;background:var(--white)}
.bottom-bar p{position:absolute;left:80px;top:26px;font-size:12px;color:#333}
.socials{position:absolute;left:936px;top:20px;display:flex;gap:12px}
.socials i{width:26px;height:26px;border-radius:50%;background:var(--red)}
</style>
</head>
<body>

<header class="site-header">
  <div class="menu-toggle"><span></span><span></span><span></span></div>
  <div class="brand"><div class="brand-dot"></div><div class="brand-name">Pine Ridge<br>Alder Group</div></div>
  <div class="header-call">
    <div class="ic"><svg width="16" height="16" viewBox="0 0 24 24"><path fill="#fff" d="M6.6 10.8a15.1 15.1 0 006.6 6.6l2.2-2.2c.3-.3.7-.4 1-.2 1.1.4 2.3.6 3.6.6.6 0 1 .4 1 1V20c0 .6-.4 1-1 1A17 17 0 013 4c0-.6.4-1 1-1h3.5c.6 0 1 .4 1 1 0 1.3.2 2.5.6 3.6.1.3 0 .7-.2 1z"/></svg></div>
    <p>Confidential Financial<br>Review <span>Call Now</span><br><b>916.555.0142</b></p>
  </div>
</header>

<section class="hero" role="img" aria-label="Hand holding a tablet with a glowing rising stock chart">
  <div class="hero-caption">Winning Strategies with<br>Pine Ridge Alder Group</div>
  <svg class="hero-arrow" style="left:40px" width="24" height="40" viewBox="0 0 24 40"><path d="M20 4L4 20l16 16" stroke="#fff" stroke-width="4" fill="none"/></svg>
  <svg class="hero-arrow" style="left:1136px" width="24" height="40" viewBox="0 0 24 40"><path d="M4 4l16 16L4 36" stroke="#fff" stroke-width="4" fill="none"/></svg>
  <div class="hero-dots"><i></i><i></i><i></i></div>
</section>

<h2 class="services-title">Our Services:</h2>
<svg width="0" height="0" style="position:absolute"><defs><symbol id="tick" viewBox="0 0 20 20"><rect x="1.5" y="3.5" width="14" height="14" fill="none" stroke="#e8282e" stroke-width="2"/><path d="M5 10l4 4 9-11" fill="none" stroke="#e8282e" stroke-width="2.6"/></symbol></defs></svg>
<div class="service" style="left:95px;top:802px"><svg width="22" height="22"><use href="#tick"/></svg>Tax Strategy</div>
<div class="service" style="left:95px;top:862px"><svg width="22" height="22"><use href="#tick"/></svg>Predictable Retirement Solutions</div>
<div class="service" style="left:95px;top:924px"><svg width="22" height="22"><use href="#tick"/></svg>Business Tax Avoidance</div>
<div class="service" style="left:95px;top:985px"><svg width="22" height="22"><use href="#tick"/></svg>Liability</div>
<div class="service" style="left:616px;top:802px"><svg width="22" height="22"><use href="#tick"/></svg>Legacy Planning</div>
<div class="service" style="left:616px;top:862px"><svg width="22" height="22"><use href="#tick"/></svg>Superior College Saving Plans</div>
<div class="service" style="left:616px;top:924px"><svg width="22" height="22"><use href="#tick"/></svg>Fee-less Portfolio Management</div>
<div class="service" style="left:616px;top:985px"><svg width="22" height="22"><use href="#tick"/></svg>Market Crash Protection</div>

<section class="contact-band">
  <h2>Contact us at</h2>
  <div class="contact-row">
    <span><i class="round-ic"><svg width="28" height="20" viewBox="0 0 28 20"><rect width="28" height="20" rx="2" fill="#fff"/><path d="M1 1l13 10L27 1" stroke="#e8282e" stroke-width="2" fill="none"/></svg></i>Sales@PRAlderGroup.com</span>
    <span><i class="round-ic"><svg width="28" height="28" viewBox="0 0 24 24"><path fill="#fff" d="M6.6 10.8a15.1 15.1 0 006.6 6.6l2.2-2.2c.3-.3.7-.4 1-.2 1.1.4 2.3.6 3.6.6.6 0 1 .4 1 1V20c0 .6-.4 1-1 1A17 17 0 013 4c0-.6.4-1 1-1h3.5c.6 0 1 .4 1 1 0 1.3.2 2.5.6 3.6.1.3 0 .7-.2 1z"/></svg></i>916.555.0142</span>
  </div>
  <p class="tag">Secure Your 401 K</p>
</section>

<section class="features">
  <div class="feature" style="left:79px">
    <svg width="44" height="44" viewBox="0 0 44 44"><path d="M4 40h36" stroke="#e8282e" stroke-width="3"/><rect x="8" y="24" width="6" height="14" fill="#e8282e"/><rect x="18" y="16" width="6" height="22" fill="#e8282e"/><rect x="28" y="20" width="6" height="18" fill="#e8282e"/><path d="M6 18l10-10 8 6 14-10" stroke="#e8282e" stroke-width="2.5" fill="none"/></svg>
    <p>Insuring Portfolios Against Market Crashes</p>
  </div>
  <div class="feature" style="left:344px">
    <svg width="44" height="44" viewBox="0 0 44 44"><path d="M12 6v22h20M12 18h18v10M14 28l-4 12M30 28l4 12M6 40c10 2 22 2 32 0" stroke="#e8282e" stroke-width="3" fill="none"/></svg>
    <p>Seemingly Small Fees Devastate Retirements.</p>
  </div>
  <div class="feature" style="left:609px">
    <svg width="50" height="44" viewBox="0 0 50 44"><rect x="4" y="4" width="42" height="36" rx="3" fill="none" stroke="#e8282e" stroke-width="3"/><rect x="12" y="10" width="26" height="10" fill="#e8282e"/><path d="M12 27h26M12 33h18" stroke="#e8282e" stroke-width="2.5"/></svg>
    <p>Business Owners &amp; Executives Love Our Tax &amp; Bonus Strategies!</p>
  </div>
  <div class="feature" style="left:874px">
    <svg width="44" height="44" viewBox="0 0 44 44"><circle cx="22" cy="12" r="8" fill="#e8282e"/><path d="M22 20v10" stroke="#e8282e" stroke-width="3"/><path d="M12 30h20l-3 12H15z" fill="#e8282e"/></svg>
    <p>401K, Mutual Fund &amp; IRA Myths Revealed</p>
  </div>
</section>

<h2 class="section-band" style="top:1633px;height:64px">Blogs, Videos &amp; Radio</h2>

<article class="blog-card" style="left:71px">
  <div class="blog-media" role="img" aria-label="Radio show artwork" style="background:linear-gradient(135deg,#f7f7f7,#e9e9e9)"></div>
  <h3>Harbor Radio</h3>
  <p>Catch us on Harbor Radio's Lena Marsh Show, now on the Harbor Radio Network. Tune in with us every weekend morning for fresh money talk.</p>
  <p>Pine Ridge Alder Group's Money Minded Mike &amp; Everyday Eddie will make your weekend morning and financial future yodel</p>
</article>
<article class="blog-card" style="left:436px">
  <div class="blog-media" role="img" aria-label="Portrait of a smiling advisor at his desk" style="background:linear-gradient(135deg,#d9dde3,#8d96a2)"></div>
  <h3>PRAG Videos</h3>
  <p>Here you can find quick videos expanding on some of our strategies, philosophies &amp; products. We are currently under re-construction. Please come back and visit us in a week.</p>
</article>
<article class="blog-card" style="left:796px">
  <div class="blog-media" role="img" aria-label="Businessman celebrating under falling banknotes" style="background:linear-gradient(135deg,#e8e8e8,#a9aba8)"></div>
  <h3>Money Blog</h3>
  <p>Ever start to think that portfolio and investing is so confusing that you need a financial advisor to help them to your money? Maybe it's by design. Get educated on our blog. Time to get in touch, stay in touch and get educated about your money. Your education is our advantage. Check out our extremely educational and entertaining Money Series with Money Minded Mike and Everyday Eddie.</p>
</article>

<div class="pill" style="left:502px;top:2283px;width:204px;height:37px">401k Facts</div>

<h2 class="section-band" style="top:2373px;height:61px">Retirement Calculators</h2>

<section class="calc">
  <div class="calc-row"><h4>Retirement plan inputs:</h4><p style="text-align:center">Retire at age 67 with 90% of current income</p><span class="ctl">✎ [+]</span></div>
  <div class="calc-row"><h4>Investment returns, inflation and Social Security:</h4><p style="text-align:center">7% pre-retirement, 4% in retirement, 2.9% inflation, Include Social Security? No</p><span class="ctl">✎ [+]</span></div>
  <div class="calc-row"><h4 style="text-align:center">Retirement savings runs out at age 76.</h4><p>Your plan provides $624,048 when you retire. This assumes annual retirement expenses of $68,205 which is 90% of your last year's income of $75,783. This includes $0 per year from Social Security.</p><span class="ctl">▮ [+]</span></div>
</section>

<h2 class="section-band" style="top:2846px;height:61px">Testimonials</h2>

<article class="testimonial" style="left:114px">
  <div class="avatar" role="img" aria-label="Client portrait"></div>
  <h5>Dale Hensley</h5>
  <p>National Business Alliance Turnaround CEO of the Year<br>I'm a CFO by trade. PRAG has strategies for families, executive &amp; business owners that accountants and financial advisors don't have. Highest recommendation.</p>
</article>
<article class="testimonial" style="left:447px">
  <div class="avatar" role="img" aria-label="Client portrait"></div>
  <h5>Mark Tolliver</h5>
  <p>Probate Attorney. As an attorney, my job is to weigh risk. As an investor, weighing risk and reward is even more important. As someone retiring in next 15 years, I wanted to eliminate the risks of a stock market crash. PRAG does this better than any other company.</p>
</article>
<article class="testimonial" style="left:780px">
  <div class="avatar" role="img" aria-label="Client portrait"></div>
  <h5>Paul Brenner</h5>
  <p>Doctor. Being a doctor requires attention to detail. Pine Ridge Alder Group helped navigate and educate me on exactly how to decipher my portfolio statement. I would have changed 10 years ago if I would have known what I know now about money. Call them, you'll be happy you did</p>
</article>
<div class="t-dots"><i></i><i></i><i></i></div>

<div class="quick-email">Shoot us a quick email here</div>
<div class="pill" style="left:735px;top:3410px;width:158px;height:37px">Submit</div>

<div class="call-us">CALL US <i class="round-ic"><svg width="28" height="28" viewBox="0 0 24 24"><path fill="#fff" d="M6.6 10.8a15.1 15.1 0 006.6 6.6l2.2-2.2c.3-.3.7-.4 1-.2 1.1.4 2.3.6 3.6.6.6 0 1 .4 1 1V20c0 .6-.4 1-1 1A17 17 0 013 4c0-.6.4-1 1-1h3.5c.6 0 1 .4 1 1 0 1.3.2 2.5.6 3.6.1.3 0 .7-.2 1z"/></svg></i> 916.555.0142</div>

<footer class="site-footer">
  <div class="foot-brand"><span class="dot"></span><span>Pine Ridge<br>Alder Group</span></div>
  <p class="foot-about">Bringing sensibility, predictability and peace of mind in retirement. We will do things for your financial lives accountants and financial advisors won't and can't.</p>
  <div class="foot-col" style="left:404px">
    <h6>Quick Link</h6>
    <ul><li>Home</li><li>Insuring Portfolios</li><li>Small Fees</li><li>Business Owners</li><li>401K</li><li>Services</li><li>Contact us</li></ul>
  </div>
  <div class="foot-col" style="left:571px">
    <h6>Address</h6>
    <p class="addr">⌖ 4821 Calder Road,<br>&nbsp;&nbsp;&nbsp;Oak Valley,<br>&nbsp;&nbsp;&nbsp;CA 95610<br>☏ 916.555.0142<br>✉ Sales@PRAlderGroup.com</p>
  </div>
  <div class="foot-col" style="left:825px">
    <h6>Contact us</h6>
    <div style="display:flex;gap:6px;width:296px"><div class="field" style="flex:1">Name</div><div class="field" style="flex:1">Email</div><div class="field" style="flex:1">Phone</div></div>
    <div class="field" style="width:296px;height:66px;margin-top:6px">Message</div>
    <div class="pill" style="position:static;width:176px;height:32px;margin-top:10px;font-size:13px">Baby Boomer Edition</div>
  </div>
</footer>

<div class="bottom-bar">
  <p>Copyright © 2019 Pine Ridge Alder Group. All Right Reserve</p>
  <div class="socials"><i></i><i></i><i></i><i></i><i></i></div>
</div>

</body>
</html>
```